i would like a business card to leave with customers and potential customers for electrical work and for the supply and install of reverse cycle airconditioning in the domestic and commercial market.
I own my own business and im a sole trader. I have an a'class electrical lisence and also a refrigeration lisence so i am
able to offer complete installations in airconditioning by a fully qualified and lisenced tradesman.
im looking for something that comes across as unique and professional.
i had the coluor black and some gold in mind but open to any coluors.
something like Beacon Electrical & Refrigeration
or Beacon Air.
i will use this design on a business card to advertise through summer to help generate installs through the busy season.

Target Market(s)

Mainly domestic house holds through summer who are in need of airconditioning and reliable information to acomadate thier cooling and heating requirements

Industry/Entity Type

Electrical

Requirements
Must have
• Business name- Beacon
My name- Peter Wollaston
My mobile no- 0457 819 302
My email- prwollaston@tarvel.com.au
Installation & Decomissioning of aiconditioning split systems
LIC NO: KTR 407516
Nice to have
• Beacon Electrical & Refrigeration

```html
<!DOCTYPE html>
<html lang="en">
<head>
<meta charset="utf-8">
<title>Beacon Electrical &amp; Refrigeration – Business Card</title>
<link rel="stylesheet" href="https://fonts.googleapis.com/css2?family=Italianno&family=Arimo:ital@0;1&display=swap">
<style>
  :root {
    --page: #ffffff;
    --frame: #e4e8d2;
    --card: #ffffff;
    --gold: #f3b912;
    --ink: #1a1a1a;
    --unit-light: #fbfbfb;
    --unit-mid: #e9e9e9;
    --unit-edge: #d4d4d4;
    --bag-red: #d8323a;
    --bag-dark: #b3222a;
    --badge-blue: #2aa6df;
    --badge-base: #1a1a1a;
  }
  html, body {
    margin: 0;
    padding: 0;
    width: 721px;
    height: 1200px;
    overflow: hidden;
    background: var(--page);
  }
  .canvas {
    position: relative;
    width: 721px;
    height: 1200px;
    font-family: "Arimo", Arial, sans-serif;
    color: var(--ink);
  }
  .frame {
    position: absolute;
    left: 38px; top: 38px;
    width: 647px; height: 1128px;
    background: var(--frame);
  }
  .card {
    position: absolute;
    left: 68px; top: 64px;
    width: 582px; height: 1070px;
    background: var(--card);
    border-radius: 38px;
  }
  .art-outdoor-unit {
    position: absolute;
    left: 188px; top: 90px;
    width: 250px; height: 168px;
    border-radius: 6px;
    background: linear-gradient(180deg, var(--unit-light) 0%, var(--unit-mid) 100%);
    box-shadow: inset 0 0 0 1px var(--unit-edge);
  }
  .art-indoor-unit {
    position: absolute;
    left: 289px; top: 207px;
    width: 334px; height: 114px;
    border-radius: 12px 12px 18px 18px;
    background: linear-gradient(180deg, var(--unit-light) 0%, var(--unit-mid) 100%);
    box-shadow: inset 0 0 0 1px var(--unit-edge), 0 3px 6px rgba(0,0,0,0.12);
  }
  .art-toolbag {
    position: absolute;
    left: 88px; top: 300px;
    width: 286px; height: 250px;
    border-radius: 40% 40% 22px 22px / 30% 30% 22px 22px;
    background: radial-gradient(ellipse at 50% 65%, var(--bag-red) 0%, var(--bag-dark) 70%, rgba(179,34,42,0.85) 100%);
  }
  .name-band {
    position: absolute;
    left: 38px; top: 561px;
    width: 636px; height: 114px;
    background: var(--gold);
    border: 4px solid #ffffff;
    border-radius: 16px;
    box-shadow: 0 3px 8px rgba(0,0,0,0.35);
    display: flex;
    align-items: center;
    justify-content: center;
  }
  .business-name {
    margin: 0;
    font-family: "Italianno", cursive;
    font-weight: 400;
    font-size: 64px;
    color: var(--ink);
    white-space: nowrap;
  }
  .person {
    position: absolute;
    right: 118px;
    top: 725px;
    margin: 0;
    font-family: "Italianno", cursive;
    font-weight: 400;
    font-size: 58px;
    line-height: 1;
  }
  .contact {
    position: absolute;
    right: 62px;
    top: 868px;
    text-align: right;
  }
  .contact-line {
    margin: 0;
    font-size: 28px;
    line-height: 42px;
  }
  .badge {
    position: absolute;
    left: 100px; top: 1014px;
    width: 98px; height: 112px;
  }
  .service {
    position: absolute;
    left: 196px; top: 1018px;
    width: 400px;
    text-align: center;
    font-style: italic;
    font-size: 25px;
    line-height: 38px;
  }
  .service p { margin: 0; }
</style>
</head>
<body>
<div class="canvas">
  <div class="frame"></div>
  <div class="card"></div>

  <div class="art-outdoor-unit" role="img" aria-label="Illustration of an air conditioner outdoor unit"></div>
  <div class="art-indoor-unit" role="img" aria-label="Illustration of a split system indoor wall unit"></div>
  <div class="art-toolbag" role="img" aria-label="Illustration of a red tradesman's tool bag full of tools"></div>

  <div class="name-band">
    <h1 class="business-name">Beacon Electrical &amp; Refrigeration</h1>
  </div>

  <p class="person">Peter Wollaston</p>

  <div class="contact">
    <p class="contact-line">mobile: 0457 819 302</p>
    <p class="contact-line">email: prwollaston@tarvel.com.au</p>
  </div>

  <svg class="badge" viewBox="0 0 98 112" role="img" aria-label="Authorised installer badge">
    <rect x="0" y="0" width="98" height="88" fill="var(--badge-blue)"/>
    <rect x="0" y="92" width="98" height="20" fill="var(--badge-base)"/>
  </svg>

  <div class="service">
    <p>Installation &amp; Decomissioning of</p>
    <p>aiconditioning split systems</p>
    <p>LIC NO: KTR 407516</p>
  </div>
</div>
</body>
</html>
```